UK Online Auction Site needs a clever design

We need a contemporary landing page and registration page design for a UK auction website, that look equally at home on PC's and tablets . The design should be fresh, bright, clean, professional, robust, and familiar. We would like to see something clever but functional.

```html
<!DOCTYPE html>
<html lang="en">
<head>
<meta charset="utf-8">
<title>Bidwell – UK Online Auctions</title>
<link href="https://fonts.googleapis.com/css2?family=Open+Sans:wght@400;600;700&display=swap" rel="stylesheet">
<style>
:root{
  --blue:#0c9ddc;
  --blue-dark:#0a86bd;
  --ink:#222;
  --muted:#8a8a8a;
  --hero-bg:#ececec;
  --band-bg:#ededed;
  --line:#d8d8d8;
  --dark:#2b2b2b;
  --white:#fff;
}
*{margin:0;padding:0;box-sizing:border-box}
html,body{width:779px;height:1200px;overflow:hidden;background:var(--white)}
body{font-family:"Open Sans",Arial,sans-serif;color:var(--ink);position:relative}
.abs{position:absolute}
a{color:inherit;text-decoration:none}

.topbar{left:0;top:0;width:779px;height:16px;background:var(--blue);color:var(--white);font-size:7px;}
.topbar nav{position:absolute;left:405px;top:4px;display:flex;gap:6px}
.topbar nav span.sep{opacity:.9}

.brand{left:142px;top:30px;font-size:24px;font-weight:700;color:var(--blue);line-height:1;display:flex;align-items:center;gap:5px}
.brand i{width:10px;height:10px;border-radius:50%;background:var(--blue);display:block}
.search{left:434px;top:34px;width:186px;height:16px;background:#eaeaea;font-size:6.5px;color:#555;padding:4px 10px}
.search svg{position:absolute;right:6px;top:6px}
.search-btn{left:622px;top:34px;width:18px;height:16px;background:var(--blue)}
.search-btn svg{position:absolute;left:4px;top:3px}

.hero{left:0;top:74px;width:779px;height:218px;background:var(--hero-bg)}
.hero-photo{left:120px;top:14px;width:272px;height:196px;background:linear-gradient(180deg,#e6e1dc,#d9d4cf)}
.hero-title{left:474px;top:55px;width:188px;height:33px;background:var(--blue);color:var(--white);font-size:24px;text-align:center;line-height:33px}
.hero-text{left:436px;top:103px;width:266px;text-align:center;font-size:9px;color:#a8a8a8;line-height:12px}
.hero-btn{left:538px;top:140px;width:62px;height:15px;background:var(--blue);color:var(--white);font-size:6.5px;text-align:center;line-height:15px}
.arrow{top:96px;width:22px;height:26px;background:#cfcfcf}
.arrow svg{position:absolute;left:6px;top:7px}

.intro-img{top:322px;width:104px;height:72px;border:1px solid #e2e2e2;padding:2px}
.intro-img div{width:100%;height:100%}
.intro h3{position:absolute;top:404px;font-size:11.5px;font-weight:400;text-align:center;width:134px;white-space:nowrap}
.intro p{position:absolute;top:422px;font-size:6px;color:var(--muted);text-align:center;width:124px;line-height:8px;white-space:nowrap}
.btn-read{top:446px;width:43px;height:14px;background:var(--blue);color:var(--white);font-size:5.5px;text-align:center;line-height:14px;border-radius:1px}
.ad{left:531px;top:322px;width:105px;height:138px;background:linear-gradient(180deg,#dcdad6,#c9c6c0)}

.band{left:0;top:490px;width:779px;height:284px;background:var(--band-bg)}
.section-title{left:0;width:779px;text-align:center;font-size:16px;font-weight:400}
.rule{left:286px;width:206px;height:0;border-top:1px dotted #c8c8c8}
.rule::before,.rule::after{content:"";position:absolute;top:-3px;width:5px;height:5px;border-radius:50%;background:#ccc}
.rule::before{left:-2px}.rule::after{right:-2px}
.pager{top:549px;width:11px;height:10px;background:#d6d6d6}
.pager svg{position:absolute;left:3px;top:2px}

.card{width:118px;height:169px;background:var(--white);border:1px solid #e6e6e6}
.card .pic{position:absolute;left:4px;top:3px;width:108px;height:80px}
.card h4{position:absolute;left:8px;top:91px;font-size:7px;font-weight:400;white-space:nowrap}
.card .dash{position:absolute;left:8px;top:107px;width:102px;border-top:1px dotted #ddd}
.card .dash::before{content:"";position:absolute;left:1px;top:-2px;width:3px;height:3px;border-radius:50%;background:var(--blue)}
.card p{position:absolute;left:8px;top:114px;width:104px;font-size:5.5px;color:var(--muted);line-height:10px}
.card .price{position:absolute;left:8px;top:143px;font-size:8px;font-weight:600}
.card .buy{position:absolute;right:8px;top:143px;width:45px;height:13px;background:var(--blue);color:var(--white);font-size:5px;text-align:center;line-height:13px}

.footer{left:0;top:1074px;width:779px;height:100px;background:var(--blue);color:var(--white)}
.fcol{position:absolute;top:20px;font-size:6.5px;line-height:12.5px;white-space:nowrap}
.fcol h5{font-size:7.5px;font-weight:700;margin-bottom:1px;line-height:12px}
.social li{list-style:none;display:flex;align-items:center;gap:6px}
.social li i{width:8px;height:8px;border-radius:50%;background:var(--white);display:block}
.bottom{left:0;top:1174px;width:779px;height:26px;background:var(--dark);color:#bbb;font-size:5.5px;text-align:center;line-height:26px}
</style>
</head>
<body>

<header>
  <div class="abs topbar">
    <nav><a>SELL</a><span class="sep">|</span><a>SIGN IN</a><span class="sep">|</span><a>BASKET</a><span class="sep">|</span><a>HELP</a><span class="sep">|</span><a>CONTACT</a></nav>
  </div>
  <div class="abs brand"><i></i>Bidwell</div>
  <div class="abs search">Serach All Categories
    <svg width="6" height="4" viewBox="0 0 6 4"><path d="M0 0h6L3 4z" fill="#555"/></svg>
  </div>
  <div class="abs search-btn">
    <svg width="10" height="10" viewBox="0 0 10 10"><circle cx="4" cy="4" r="3" fill="none" stroke="#fff" stroke-width="1.5"/><path d="M6 6l3 3" stroke="#fff" stroke-width="1.8"/></svg>
  </div>
</header>

<section class="abs hero">
  <div class="abs hero-photo" role="img" aria-label="Three women modelling summer fashion outfits"></div>
  <div class="abs hero-title">Fashion</div>
  <p class="abs hero-text">Lorem ipsum dolor sit amet, consecte adipiscing elit. Fusce at justo eget lorem port titor tincidunt.</p>
  <a class="abs hero-btn">VISIT MORE</a>
  <div class="abs arrow" style="left:0"><svg width="8" height="12" viewBox="0 0 8 12"><path d="M7 0L0 6l7 6z" fill="#fff"/></svg></div>
  <div class="abs arrow" style="left:757px"><svg width="8" height="12" viewBox="0 0 8 12"><path d="M1 0l7 6-7 6z" fill="#fff"/></svg></div>
</section>

<section class="intro">
  <div class="abs intro-img" style="left:138px"><div role="img" aria-label="Group of women in fashionable outfits" style="background:linear-gradient(180deg,#d9cfc4,#b9a99a)"></div></div>
  <div class="abs intro-img" style="left:266px"><div role="img" aria-label="Assorted jewellery and accessories" style="background:linear-gradient(180deg,#e8ddd0,#c9b79d)"></div></div>
  <div class="abs intro-img" style="left:397px"><div role="img" aria-label="Pile of soft toy teddy bears" style="background:linear-gradient(180deg,#d8c7c0,#b79b8e)"></div></div>
  <h3 style="left:125px">Welcome</h3>
  <p style="left:130px">Even if you're new or already experienced,<br>we have everything</p>
  <h3 style="left:251px">Sign In</h3>
  <p style="left:256px">Sign-in to your account in order to buy,<br>sell or manage your</p>
  <h3 style="left:383px">Shop with Confidence</h3>
  <p style="left:388px">Bid on or buy items you're watching<br>or searching for</p>
  <a class="abs btn-read" style="left:164px">Read More</a>
  <a class="abs btn-read" style="left:296px">Read More</a>
  <a class="abs btn-read" style="left:426px">Read More</a>
  <div class="abs ad" role="img" aria-label="Advertisement space showing a fashion model in a patterned skirt"></div>
</section>

<section class="abs band"></section>
<h2 class="abs section-title" style="top:505px">OUR LATEST ARRIVALS</h2>
<div class="abs rule" style="top:542px"></div>
<div class="abs pager" style="left:617px"><svg width="4" height="6" viewBox="0 0 4 6"><path d="M3 0L0 3l3 3" fill="none" stroke="#fff"/></svg></div>
<div class="abs pager" style="left:630px"><svg width="4" height="6" viewBox="0 0 4 6"><path d="M1 0l3 3-3 3" fill="none" stroke="#fff"/></svg></div>

<div class="abs card" style="left:137px;top:566px"><div class="pic" role="img" aria-label="Checked strapless dress" style="background:linear-gradient(180deg,#b9c3c4,#8e9ea3)"></div><h4>Modern Dress</h4><div class="dash"></div><p>Lorem ipsum dolor sit amet, cocteru adipiscing elit.</p><span class="price">$59.89</span><a class="buy">BUY NOW</a></div>
<div class="abs card" style="left:266px;top:566px"><div class="pic" role="img" aria-label="Sports kit with gloves and balls" style="background:linear-gradient(180deg,#c7a88d,#8a5a3f)"></div><h4>Sports kit</h4><div class="dash"></div><p>Lorem ipsum dolor sit amet, cocteru adipiscing elit.</p><span class="price">$159.89</span><a class="buy">BUY NOW</a></div>
<div class="abs card" style="left:395px;top:566px"><div class="pic" role="img" aria-label="Black leather shoulder bag" style="background:linear-gradient(180deg,#6b6562,#2e2a29)"></div><h4>Leather Bag</h4><div class="dash"></div><p>Lorem ipsum dolor sit amet, cocteru adipiscing elit.</p><span class="price">$24.89</span><a class="buy">BUY NOW</a></div>
<div class="abs card" style="left:524px;top:566px"><div class="pic" role="img" aria-label="Silver handheld camcorder" style="background:linear-gradient(180deg,#c8cacd,#7d8186)"></div><h4>Soft Toy</h4><div class="dash"></div><p>Lorem ipsum dolor sit amet, cocteru adipiscing elit.</p><span class="price">$2559.89</span><a class="buy">BUY NOW</a></div>

<h2 class="abs section-title" style="top:798px">OUR FEATURED PRODUCTS</h2>
<div class="abs rule" style="top:835px"></div>

<div class="abs card" style="left:137px;top:859px"><div class="pic" role="img" aria-label="Compact black laptop" style="background:linear-gradient(180deg,#8f9396,#3b3d40)"></div><h4>Laptop</h4><div class="dash"></div><p>Lorem ipsum dolor sit amet, cocteru adipiscing elit.</p><span class="price">$59.89</span><a class="buy">BUY NOW</a></div>
<div class="abs card" style="left:266px;top:859px"><div class="pic" role="img" aria-label="Cream teddy bear" style="background:linear-gradient(180deg,#f3dcb8,#e0b97f)"></div><h4>Teddy Bear</h4><div class="dash"></div><p>Lorem ipsum dolor sit amet, cocteru adipiscing elit.</p><span class="price">$159.89</span><a class="buy">BUY NOW</a></div>
<div class="abs card" style="left:395px;top:859px"><div class="pic" role="img" aria-label="Pink draped top" style="background:linear-gradient(180deg,#f48cb7,#d8336f)"></div><h4>Beautiful Top</h4><div class="dash"></div><p>Lorem ipsum dolor sit amet, cocteru adipiscing elit.</p><span class="price">$24.89</span><a class="buy">BUY NOW</a></div>
<div class="abs card" style="left:524px;top:859px"><div class="pic" role="img" aria-label="Silver ring with blue gemstone" style="background:linear-gradient(180deg,#dfe3e6,#6fb6d6)"></div><h4>Silver Ring with blue Diamond</h4><div class="dash"></div><p>Lorem ipsum dolor sit amet, cocteru adipiscing elit.</p><span class="price">$2559.89</span><a class="buy">BUY NOW</a></div>

<footer class="abs footer">
  <div class="fcol" style="left:140px;width:80px;white-space:normal"><h5>bidwell.co.uk</h5><p style="line-height:10.5px;margin-top:4px">Lorem ipsum dolor sit amet,cocterua dipiscing elit.</p></div>
  <div class="fcol" style="left:236px"><h5 style="margin-left:1px">Buy</h5>Categories<br>Search<br>Currency Converter</div>
  <div class="fcol" style="left:327px"><h5>Sell</h5>Sell New Item<br>Sell Bulk Items</div>
  <div class="fcol" style="left:424px"><h5>Support</h5>Contact<br>Terms<br>Privacy<br>RSS</div>
  <div class="fcol" style="left:502px"><h5>Other</h5>About<br>News<br>Feeds</div>
  <div class="fcol social" style="left:575px"><h5 style="margin-left:2px">Stay connected</h5><ul><li><i></i>Circlet</li><li><i></i>Chirper</li><li><i></i>RSS</li></ul></div>
</footer>
<div class="abs bottom">Copy right @ 2014 by Bidwell | All Rights Reserved</div>

</body>
</html>
```